Brevanta needs a business Card Design

We are looking for a business card Design for our new Managed Service Provider Company, Brevanta. Brevanta encompasses everything IT for the average medium sized business. Our primary services are help desk support, cyber-security (malware and ransomware protection), and Disaster Recovery systems. We would like the design to have a very clean and professional look, with a very minimalist feel.

Target Market(s)

Medium to large sized businesses

Industry/Entity Type

It Service

Contact Information for Business Card

Name GoesHere
name@brevanta-mail.net
O: 555-382-6047
C: 555-000-0000

Font styles to use
Other font styles liked:
• Poppins Font Only Please

Colors

Designer to choose only greyscale colors for use in the design.

Requirements
Must have
• Logo included
Nice to have
• Cutting Edge, innovative, minimalistic, elegant

```html
<!DOCTYPE html>
<html lang="en">
<head>
<meta charset="utf-8">
<title>Brevanta — Business Card</title>
<link rel="stylesheet" href="https://fonts.googleapis.com/css2?family=Poppins:wght@400;500&display=swap">
<style>
  :root {
    --backdrop: #d9d6d2;
    --card: #efeeec;
    --card-edge: #f8f7f5;
    --ink: #1e262d;
    --ink-soft: #4b5359;
  }
  * { margin: 0; padding: 0; box-sizing: border-box; }
  html, body {
    width: 1200px;
    height: 1200px;
    overflow: hidden;
    background: var(--backdrop);
    font-family: "Poppins", sans-serif;
    color: var(--ink);
  }
  .business-card {
    position: absolute;
    left: 60px;
    top: 305px;
    width: 1080px;
    height: 590px;
    background: var(--card);
    border: 2px solid var(--card-edge);
    border-radius: 22px;
    box-shadow: 0 18px 40px rgba(0, 0, 0, 0.08);
  }
  .brand {
    position: absolute;
    left: 60px;
    top: 50px;
    width: 340px;
    display: flex;
    flex-direction: column;
    align-items: center;
  }
  .brand-square {
    width: 46px;
    height: 46px;
    background: var(--ink);
    margin-bottom: 40px;
  }
  .brand-name {
    font-weight: 400;
    font-size: 31px;
    letter-spacing: 0.36em;
    text-transform: uppercase;
    line-height: 1;
    padding-left: 0.36em;
  }
  .person {
    position: absolute;
    left: 57px;
    top: 290px;
  }
  .person-name {
    font-weight: 500;
    font-size: 37px;
    line-height: 1.2;
    text-transform: uppercase;
  }
  .person-title {
    font-weight: 400;
    font-size: 27px;
    line-height: 1.3;
    color: var(--ink-soft);
  }
  .contact-list {
    position: absolute;
    left: 57px;
    top: 418px;
    list-style: none;
  }
  .contact-item {
    display: flex;
    align-items: center;
    gap: 8px;
    font-size: 27px;
    line-height: 42px;
    font-weight: 400;
  }
  .contact-icon {
    width: 24px;
    height: 24px;
    fill: var(--ink);
    flex: none;
  }
  .brand-accent {
    position: absolute;
    right: 90px;
    top: 135px;
    width: 320px;
    height: 320px;
    border-radius: 50%;
    border: 14px solid var(--ink);
  }
</style>
</head>
<body>
  <div class="business-card">
    <div class="brand">
      <div class="brand-square"></div>
      <div class="brand-name">Brevanta</div>
    </div>

    <div class="person">
      <div class="person-name">Dane Morlow</div>
      <div class="person-title">President</div>
    </div>

    <ul class="contact-list">
      <li class="contact-item">
        <svg class="contact-icon" viewBox="0 0 24 24" aria-hidden="true"><path d="M6.6 10.8a15.1 15.1 0 0 0 6.6 6.6l2.2-2.2a1 1 0 0 1 1-.25 11.4 11.4 0 0 0 3.6.57 1 1 0 0 1 1 1V20a1 1 0 0 1-1 1A17 17 0 0 1 3 4a1 1 0 0 1 1-1h3.5a1 1 0 0 1 1 1c0 1.25.2 2.45.57 3.57a1 1 0 0 1-.25 1z"/></svg>
        555-382-6047
      </li>
      <li class="contact-item">
        <svg class="contact-icon" viewBox="0 0 24 24" aria-hidden="true"><path d="M7 1h10a2 2 0 0 1 2 2v18a2 2 0 0 1-2 2H7a2 2 0 0 1-2-2V3a2 2 0 0 1 2-2zm0 3v14h10V4zm5 15.2a1.1 1.1 0 1 0 0 2.2 1.1 1.1 0 0 0 0-2.2z"/></svg>
        555-000-0000
      </li>
      <li class="contact-item">
        <svg class="contact-icon" viewBox="0 0 24 24" aria-hidden="true"><path d="M3 5h18a1 1 0 0 1 1 1v.4l-10 6-10-6V6a1 1 0 0 1 1-1zm-1 3.7 10 6 10-6V18a1 1 0 0 1-1 1H3a1 1 0 0 1-1-1z"/></svg>
        name@brevanta-mail.net
      </li>
    </ul>

    <div class="brand-accent" aria-hidden="true"></div>
  </div>
</body>
</html>
```